3" Round Business Card for Funeral Home

We need a business card designed for our cremation service. We would like to use a 3" round business card.

The business card will be 2-sided. One side with the logo featured prominently. The back sad will have employee name and contact info.

Templates for printing have been attached to project as well as logo

We like soft colors like the logo. Final design should promote a feeling of trust.

Industry/Entity Type

Funeral

Contact Information for Business Card

Employee Name, Phone number, email, web address

Requirements
Should not have
• any sort of funeral item such as urn, casket, hearse, tombstone

```html
<!DOCTYPE html>
<html lang="en">
<head>
<meta charset="utf-8">
<title>Round Business Card – Stillwater Path</title>
<link rel="stylesheet" href="https://fonts.googleapis.com/css2?family=Montserrat:wght@400;600&display=swap">
<style>
  :root {
    --bg: #dcdcdc;
    --card-white: #ffffff;
    --teal: #17a89c;
    --purple: #8e2a8f;
    --ink: #3a3a3a;
    --on-teal: #ffffff;
  }
  * { margin: 0; padding: 0; box-sizing: border-box; }
  html, body {
    width: 1200px;
    height: 1059px;
    overflow: hidden;
    background: var(--bg);
    font-family: "Montserrat", Arial, sans-serif;
  }
  .canvas { position: relative; width: 1200px; height: 1059px; }
  .card {
    position: absolute;
    top: 260px;
    width: 530px;
    height: 530px;
    border-radius: 50%;
  }
  .card--front { left: 42px; background: var(--card-white); }
  .card--back { left: 629px; background: var(--teal); }

  .brand-name {
    position: absolute;
    font-weight: 400;
    letter-spacing: -0.5px;
    white-space: nowrap;
  }
  .card--front .brand-name {
    left: 100px;
    top: 118px;
    font-size: 40px;
    color: var(--teal);
  }
  .card--back .brand-name {
    left: 47px;
    top: 226px;
    font-size: 50px;
    color: var(--on-teal);
  }

  .contact {
    position: absolute;
    left: 111px;
    top: 240px;
    color: var(--ink);
    font-size: 15px;
    line-height: 1.15;
  }
  .contact__name {
    font-weight: 600;
    font-size: 21px;
    letter-spacing: 0.8px;
    line-height: 1;
  }
  .contact__first { color: var(--teal); }
  .contact__last { color: var(--purple); }
  .contact__title { margin-top: 4px; letter-spacing: 0.4px; }
  .contact__address { margin-top: 18px; letter-spacing: 0.4px; }
  .contact__lines { list-style: none; margin-top: 10px; }
  .contact__lines li {
    display: flex;
    align-items: center;
    gap: 6px;
    height: 21.5px;
    letter-spacing: 0.4px;
  }
  .icon { width: 11px; height: 11px; flex: none; fill: var(--teal); }
</style>
</head>
<body>
<main class="canvas">
  <section class="card card--front" aria-label="Card front with contact details">
    <div class="brand-name">stillwaterpath.com</div>
    <div class="contact">
      <p class="contact__name"><span class="contact__first">DANIEL</span> <span class="contact__last">HARWOOD</span></p>
      <p class="contact__title">MAnaging Director</p>
      <p class="contact__address">1450 W Maple Avenue<br>Linden County name 4820</p>
      <ul class="contact__lines">
        <li>
          <svg class="icon" viewBox="0 0 12 12" aria-hidden="true"><path d="M2.5 0.5 L4.5 2.8 L3.4 4.2 C4.1 5.8 6.2 7.9 7.8 8.6 L9.2 7.5 L11.5 9.5 L10.2 11.3 C5.5 11 1 6.5 0.7 1.8 Z"/></svg>
          555-210-7394
        </li>
        <li>
          <svg class="icon" viewBox="0 0 12 12" aria-hidden="true"><path d="M0 2.5 H12 V10 H0 Z M0.8 3.2 L6 7 L11.2 3.2" fill="var(--teal)" stroke="#fff" stroke-width="0.8"/></svg>
          info@stillwaterpath.com
        </li>
        <li>
          <svg class="icon" viewBox="0 0 12 12" aria-hidden="true"><circle cx="6" cy="6" r="5.5"/><path d="M3 3 C4.5 4 4 6 5.5 6.5 C6 8 4.5 9 5 10.5 M8 2 C7.5 3.5 9 4 10.5 4.5" stroke="#fff" stroke-width="0.9" fill="none"/></svg>
          www.stillwaterpath.com
        </li>
      </ul>
    </div>
  </section>

  <section class="card card--back" aria-label="Card back with company name">
    <div class="brand-name">stillwaterpath.com</div>
  </section>
</main>
</body>
</html>
```